Criminal Defense Lawyer needs business cards and stationary
Dunmore Law Office
Criminal Defense Lawyer needs business cards and stationary - Law
Creative Brief
Simple
Ray Dunmore
418 N Willowbend Ave Lincoln, IL 62871
ray@dunmorelawoffice.example
dunmorelawoffice.example
I would like a simple/modern design for the front side of my card. I am thinking simply my logo in white with a blue background (same blue as in my logo). Other background colors to be considered are black and gray. That said, please be creative, I am open to any cutting edge design as long as it is not busy.
On the reverse side I would like my contact information displayed to include: My Name (Ray Dunmore) Dunmore Law Office (optional depending on design of front of card) Phone: 217-555-0176 email: ray@dunmorelawoffice.example Website: DunmoreLawOffice.example I do not want my address included. I am looking to create a visually modern yet simple design that is not too busy for the eye.
tavrelk tavrelk
Update: I have decided to add an additional winner. I will pick two designs that include business card and stationary. Thanks for the submissions. Also, designers, I am launching a website design contest soon. Keep an eye out for that.
Mistake in Brief. Please use phone number 217-555-0176 when submitting designs. Thank you.

```html
<!DOCTYPE html>
<html lang="en">
<head>
<meta charset="utf-8">
<title>Dunmore Law Office – Business Cards</title>
<link rel="stylesheet" href="https://fonts.googleapis.com/css2?family=Montserrat:wght@400;600;700&display=swap">
<style>
  :root {
    --brand-blue: #1d6f98;
    --brand-blue-dark: #155a7d;
    --paper: #ffffff;
    --ink-grey: #555b60;
    --backdrop: #e6e6e3;
  }
  * { box-sizing: border-box; margin: 0; padding: 0; }
  html, body {
    width: 1200px;
    height: 904px;
    overflow: hidden;
    background: var(--backdrop);
    font-family: "Montserrat", sans-serif;
  }
  .canvas {
    position: relative;
    width: 1200px;
    height: 904px;
  }
  .card {
    position: absolute;
    width: 560px;
    height: 320px;
    border-radius: 2px;
    box-shadow: 0 6px 18px rgba(0,0,0,0.18);
  }
  /* Front side */
  .card--front {
    left: 100px;
    top: 90px;
    background: linear-gradient(135deg, var(--brand-blue) 0%, var(--brand-blue-dark) 100%);
    color: var(--paper);
  }
  .front-brand {
    position: absolute;
    left: 0; right: 0;
    top: 112px;
    display: flex;
    align-items: center;
    justify-content: center;
    gap: 14px;
  }
  .front-brand__dot {
    width: 26px;
    height: 26px;
    border-radius: 50%;
    background: var(--paper);
  }
  .front-brand__name {
    font-weight: 700;
    font-size: 30px;
    color: var(--paper);
    letter-spacing: 0.5px;
  }
  .front-web {
    position: absolute;
    left: 0; right: 0;
    top: 208px;
    text-align: center;
    font-size: 12px;
    font-weight: 400;
    letter-spacing: 1.5px;
    color: rgba(255,255,255,0.92);
  }
  /* Back side */
  .card--back {
    left: 540px;
    top: 494px;
    background: var(--paper);
  }
  .back-brand {
    position: absolute;
    left: 40px;
    top: 150px;
    display: flex;
    align-items: center;
    gap: 10px;
  }
  .back-brand__dot {
    width: 20px;
    height: 20px;
    border-radius: 50%;
    background: var(--brand-blue);
  }
  .back-brand__name {
    font-weight: 700;
    font-size: 19px;
    color: var(--brand-blue);
    line-height: 1.15;
  }
  .contact {
    position: absolute;
    left: 330px;
    top: 140px;
    color: var(--ink-grey);
  }
  .contact__name {
    font-size: 14px;
    font-weight: 600;
    color: var(--brand-blue);
    margin-bottom: 8px;
  }
  .contact__row {
    display: flex;
    align-items: center;
    gap: 8px;
    font-size: 11.5px;
    line-height: 20px;
  }
  .contact__icon {
    width: 13px;
    height: 13px;
    flex: none;
  }
</style>
</head>
<body>
<main class="canvas">

  <section class="card card--front" aria-label="Business card front">
    <div class="front-brand">
      <span class="front-brand__dot"></span>
      <span class="front-brand__name">Dunmore</span>
    </div>
    <p class="front-web">DunmoreLawOffice.example</p>
  </section>

  <section class="card card--back" aria-label="Business card back">
    <div class="back-brand">
      <span class="back-brand__dot"></span>
      <span class="back-brand__name">Dunmore Law Office</span>
    </div>

    <div class="contact">
      <p class="contact__name">Ray Dunmore</p>
      <p class="contact__row">
        <svg class="contact__icon" viewBox="0 0 16 16" aria-hidden="true">
          <circle cx="8" cy="8" r="8" fill="#1d6f98"/>
          <path d="M5 4.5c.4-.4.9-.3 1.1.1l.7 1.3c.2.3.1.7-.2.9l-.5.4c.4.9 1.1 1.7 2 2.1l.4-.5c.2-.3.6-.4.9-.2l1.3.7c.4.2.5.7.1 1.1l-.6.6c-.5.5-1.3.5-2 .2C6.6 10.5 5.5 9.4 4.8 7.9c-.3-.7-.3-1.5.2-2z" fill="#fff"/>
        </svg>
        217-555-0176
      </p>
      <p class="contact__row">
        <svg class="contact__icon" viewBox="0 0 16 16" aria-hidden="true">
          <circle cx="8" cy="8" r="8" fill="#1d6f98"/>
          <rect x="4" y="5" width="8" height="6" rx="0.8" fill="#fff"/>
          <path d="M4.3 5.4 8 8.3l3.7-2.9" stroke="#1d6f98" stroke-width="0.9" fill="none"/>
        </svg>
        ray@dunmorelawoffice.example
      </p>
      <p class="contact__row">
        <svg class="contact__icon" viewBox="0 0 16 16" aria-hidden="true">
          <circle cx="8" cy="8" r="8" fill="#1d6f98"/>
          <circle cx="8" cy="8" r="4" fill="none" stroke="#fff" stroke-width="0.9"/>
          <path d="M4 8h8M8 4c-1.6 2.2-1.6 5.8 0 8M8 4c1.6 2.2 1.6 5.8 0 8" fill="none" stroke="#fff" stroke-width="0.9"/>
        </svg>
        DunmoreLawOffice.example
      </p>
    </div>
  </section>

</main>
</body>
</html>
```